Kelderby Farm

Need a nice simple clean double sided business card that has our logo and info on:
Kelder By Farm
Martin & Lydia Okerlund
kelderbyfarm@examplemail.test
Martin: 1-555-218-4391
Lydia: 1-555-903-2657
Instagram @ kelderby_farm

Contact Information for Business Card

Martin & Lydia Okerlund kelderbyfarm@examplemail.test Martin: 1-555-218-4391 Lydia: 1-555-903-2657

```html
<!DOCTYPE html>
<html lang="en">
<head>
<meta charset="utf-8">
<title>Kelder By Farm – Business Card</title>
<link rel="stylesheet" href="https://fonts.googleapis.com/css2?family=Cinzel:wght@500&family=Noto+Sans:wght@400&display=swap">
<style>
  :root {
    --backdrop: #e6e6e6;
    --farm-green: #5f9e41;
    --farm-green-light: #78b25c;
    --harvest-orange: #f0a21e;
    --card-white: #f4f4f4;
    --ink: #333333;
    --paper: #ffffff;
  }
  * { box-sizing: border-box; margin: 0; padding: 0; }
  html, body {
    width: 1200px; height: 960px; overflow: hidden;
    background: var(--backdrop);
  }
  .canvas { position: relative; width: 1200px; height: 960px; }
  .card {
    position: absolute; left: 309px; width: 584px; height: 334px; overflow: hidden;
  }
  .card--front { top: 124px; background: var(--farm-green); }
  .card--back { top: 509px; background: var(--card-white); }

  .front-texture {
    position: absolute; right: 0; top: 0; width: 200px; height: 334px;
    background: radial-gradient(ellipse at 60% 50%, rgba(255,255,255,0.13), rgba(255,255,255,0) 70%);
  }
  .brand-ring {
    position: absolute; border-radius: 50%;
  }
  .card--front .brand-ring {
    left: 231px; top: 80px; width: 122px; height: 122px; border: 4px solid var(--paper);
  }
  .brand-name {
    position: absolute; font-family: "Cinzel", "Times New Roman", serif; font-weight: 500;
    white-space: nowrap; text-align: center; line-height: 1;
  }
  .card--front .brand-name {
    left: 0; width: 584px; top: 205px; font-size: 33px; color: var(--paper); letter-spacing: 0.5px;
  }
  .brand-tagline {
    position: absolute; font-family: "Noto Sans", Arial, sans-serif; text-align: center;
    white-space: nowrap; line-height: 1;
  }
  .card--front .brand-tagline {
    left: 0; width: 584px; top: 244px; font-size: 16px; letter-spacing: 4.6px; color: var(--paper);
  }

  .card--back .brand-ring {
    left: 111px; top: 105px; width: 86px; height: 86px; border: 3px solid var(--farm-green);
  }
  .card--back .brand-name {
    left: 30px; width: 248px; top: 195px; font-size: 23px; color: var(--farm-green);
  }
  .card--back .brand-tagline {
    left: 30px; width: 248px; top: 222px; font-size: 11px; letter-spacing: 3.4px; color: var(--harvest-orange);
  }
  .divider { position: absolute; left: 290px; width: 2px; }
  .divider--top { top: 95px; height: 52px; background: var(--harvest-orange); }
  .divider--bottom { top: 153px; height: 87px; background: var(--farm-green); }

  .owners {
    position: absolute; left: 319px; top: 97px;
    font-family: "Cinzel", "Times New Roman", serif; font-weight: 500; font-size: 20px; line-height: 25px;
  }
  .owners__given { color: var(--farm-green); }
  .owners__family { color: var(--harvest-orange); }

  .contact-list {
    position: absolute; left: 319px; top: 160px; list-style: none;
    font-family: "Noto Sans", Arial, sans-serif; font-size: 13.5px; color: var(--ink); line-height: 19.5px;
  }
  .contact-list li { display: flex; align-items: center; gap: 5px; white-space: nowrap; }
  .contact-list svg { flex: none; }
  .contact-list .who { color: var(--farm-green); }
</style>
</head>
<body>
<main class="canvas">
  <section class="card card--front" aria-label="Card front">
    <div class="front-texture" role="img" aria-label="Faint wheat stalk decoration"></div>
    <div class="brand-ring" aria-hidden="true"></div>
    <p class="brand-name">Kelder By Farm</p>
    <p class="brand-tagline">STONE MILLED FLOUR</p>
  </section>

  <section class="card card--back" aria-label="Card back">
    <div class="brand-ring" aria-hidden="true"></div>
    <p class="brand-name">Kelder By Farm</p>
    <p class="brand-tagline">STONE MILLED FLOUR</p>

    <div class="divider divider--top"></div>
    <div class="divider divider--bottom"></div>

    <p class="owners">
      <span class="owners__given">Martin &amp; Lydia</span><br>
      <span class="owners__family">Okerlund</span>
    </p>

    <ul class="contact-list">
      <li>
        <svg width="12" height="14" viewBox="0 0 12 14" aria-hidden="true"><rect x="2.5" y="0.8" width="7" height="12.4" rx="1.4" fill="none" stroke="#f0a21e" stroke-width="1.4"/><line x1="5" y1="11" x2="7" y2="11" stroke="#f0a21e" stroke-width="1.2"/></svg>
        <span>1-555-218-4391 <span class="who">Martin</span></span>
      </li>
      <li>
        <svg width="12" height="14" viewBox="0 0 12 14" aria-hidden="true"><rect x="2.5" y="0.8" width="7" height="12.4" rx="1.4" fill="none" stroke="#f0a21e" stroke-width="1.4"/><line x1="5" y1="11" x2="7" y2="11" stroke="#f0a21e" stroke-width="1.2"/></svg>
        <span>1-555-903-2657 <span class="who">Lydia</span></span>
      </li>
      <li>
        <svg width="13" height="14" viewBox="0 0 13 14" aria-hidden="true"><rect x="0.7" y="3" width="11.6" height="8.4" fill="none" stroke="#f0a21e" stroke-width="1.4"/><polyline points="0.7,3 6.5,8 12.3,3" fill="none" stroke="#f0a21e" stroke-width="1.4"/></svg>
        <span>kelderbyfarm@examplemail.test</span>
      </li>
      <li>
        <svg width="13" height="14" viewBox="0 0 13 14" aria-hidden="true"><rect x="1" y="1.5" width="11" height="11" fill="none" stroke="#f0a21e" stroke-width="1.6"/></svg>
        <span>@kelderby_farm</span>
      </li>
    </ul>
  </section>
</main>
</body>
</html>
```